New Coffee Packaging

Update/refresh/modernize range of 1 kg Coffee packaging

Industry/Entity Type

Hospitalty

Requirements
Must have
• Clean. crisp, eye catching
Nice to have
• Vendra means 'Height' specialty coffee is grown at high altitudes, peaks. mountains

```html
<!DOCTYPE html>
<html lang="en">
<head>
<meta charset="utf-8">
<title>Vendra Coffee Co. – Summit 1 kg Pack</title>
<link href="https://fonts.googleapis.com/css2?family=Saira+Semi+Condensed:wght@500;600&family=Federo&family=Montserrat:wght@400;700&family=Oswald:wght@300;500&display=swap" rel="stylesheet">
<style>
  :root {
    --backdrop: #fdf4d4;
    --paper: #f3f3f1;
    --gold: #b8862f;
    --gold-soft: #d9b574;
    --ink: #111111;
    --text: #2a2a2a;
  }
  * { box-sizing: border-box; margin: 0; padding: 0; }
  html, body { width: 899px; height: 1200px; overflow: hidden; }
  body {
    background: var(--backdrop);
    position: relative;
    font-family: "Montserrat", sans-serif;
    color: var(--text);
  }
  .panel {
    position: absolute;
    top: 110px;
    width: 400px;
    height: 980px;
    background: var(--paper);
    overflow: hidden;
    box-shadow: 0 6px 24px rgba(120, 90, 30, 0.15);
  }
  .panel--front { left: 28px; }
  .panel--back { left: 471px; }

  /* Front */
  .brand-label {
    position: absolute;
    left: 62px; top: 0;
    width: 276px; height: 360px;
    background: var(--ink);
    display: flex; flex-direction: column;
    align-items: center; justify-content: flex-end;
    padding: 0 16px 52px;
  }
  .brand-name {
    font-family: "Saira Semi Condensed", "Arial Narrow", sans-serif;
    font-weight: 600;
    color: #ffffff;
    text-align: center;
    line-height: 1;
  }
  .brand-label .brand-name { font-size: 64px; letter-spacing: 0; }
  .brand-label .brand-name span { display: block; font-size: 22px; letter-spacing: 4px; margin-top: 14px; font-weight: 500; }

  .blend-band {
    position: absolute;
    left: 0; top: 410px;
    width: 100%; height: 72px;
    background: var(--gold);
    display: flex; align-items: center; justify-content: center;
  }
  .blend-name {
    font-family: "Federo", sans-serif;
    font-size: 40px;
    font-weight: 400;
    color: #ffffff;
    letter-spacing: 1px;
  }
  .cup-profile { position: absolute; left: 58px; top: 500px; right: 30px; }
  .cup-profile h2 { font-size: 13px; font-weight: 700; letter-spacing: 0.5px; color: var(--ink); }
  .cup-profile p { font-size: 9.5px; margin-top: 6px; }

  .brew-methods {
    position: absolute; left: 0; right: 0; top: 560px;
    display: flex; justify-content: center; gap: 22px;
    list-style: none;
  }
  .brew-methods li {
    width: 44px; display: flex; flex-direction: column; align-items: center;
    font-size: 9px; color: var(--text);
  }
  .brew-methods svg { width: 26px; height: 26px; margin-bottom: 4px; }

  .front-illustration {
    position: absolute; left: 0; right: 0; bottom: 0; height: 330px;
    background: radial-gradient(ellipse at 50% 55%, var(--gold-soft) 0%, rgba(217,181,116,0.35) 55%, var(--paper) 80%);
  }

  /* Back */
  .back-illustration {
    position: absolute; left: 0; right: 0; top: 0; height: 300px;
    background: radial-gradient(ellipse at 50% 40%, var(--gold-soft) 0%, rgba(217,181,116,0.35) 55%, var(--paper) 80%);
  }
  .panel--back .brand-name {
    position: absolute; left: 0; right: 0; top: 360px;
    color: var(--ink);
    font-size: 46px;
  }
  .panel--back .brand-name span { display: block; font-size: 15px; letter-spacing: 3px; margin-top: 10px; font-weight: 500; }

  .story {
    position: absolute; left: 50px; right: 50px; top: 490px;
    font-family: "Oswald", sans-serif; font-weight: 300;
    font-size: 11.5px; line-height: 1.45;
    text-transform: uppercase; text-align: center; color: var(--ink);
  }
  .story p + p { margin-top: 12px; }
  .story strong { font-weight: 500; }

  .badges {
    position: absolute; left: 0; right: 0; top: 700px;
    display: flex; justify-content: center; gap: 30px;
  }
  .badge {
    width: 60px; height: 60px; border-radius: 50%;
    border: 3px solid var(--ink);
  }
  .badge--gold { background: var(--gold); border-color: var(--gold); }

  .web-band {
    position: absolute; left: 0; top: 800px;
    width: 100%; height: 30px;
    background: var(--gold);
    display: flex; align-items: center; justify-content: center;
    color: #ffffff; font-size: 12px; font-weight: 700; letter-spacing: 1px;
  }
</style>
</head>
<body>

<section class="panel panel--front" aria-label="Front of pack">
  <div class="brand-label">
    <p class="brand-name">Vendra<span>coffee co.</span></p>
  </div>

  <div class="blend-band"><h1 class="blend-name">Summit</h1></div>

  <div class="cup-profile">
    <h2>CUP PROFILE</h2>
    <p>Dark Chocolate | Caramel | Malt | Lower acidity and fully body</p>
  </div>

  <ul class="brew-methods">
    <li>
      <svg viewBox="0 0 26 26" fill="none" stroke="#2a2a2a" stroke-width="1.4"><path d="M3 5h20l-8 11v4h-4v-4z"/></svg>
      Filter
    </li>
    <li>
      <svg viewBox="0 0 26 26" fill="none" stroke="#2a2a2a" stroke-width="1.4"><circle cx="7" cy="8" r="4"/><path d="M10 11l13 11" stroke-width="3"/></svg>
      Espresso
    </li>
    <li>
      <svg viewBox="0 0 26 26" fill="none" stroke="#2a2a2a" stroke-width="1.4"><rect x="7" y="7" width="11" height="16"/><path d="M12 2v5M8 5h9M18 10h3v9h-3"/></svg>
      Plunger
    </li>
    <li>
      <svg viewBox="0 0 26 26" fill="#2a2a2a"><ellipse cx="9" cy="9" rx="4" ry="5.5"/><ellipse cx="16" cy="18" rx="4" ry="5.5"/></svg>
      Beans
    </li>
  </ul>

  <div class="front-illustration" role="img" aria-label="Gold line-art illustration of coffee flowers and leaves"></div>
</section>

<section class="panel panel--back" aria-label="Back of pack">
  <div class="back-illustration" role="img" aria-label="Gold line-art illustration of coffee flowers and leaves"></div>

  <p class="brand-name">Vendra<span>coffee co.</span></p>

  <div class="story">
    <p>We source our coffee direct from growers for a more traceable and ethical supply chain.</p>
    <p>We roast our coffee to a specific profile, bringing out its natural characteristics and flavours, resulting in the perfect cup.</p>
    <p><strong>We believe this provides us with the finest coffee possible.</strong></p>
    <p>Our coffee is 100% New Zealand owned and operated.</p>
  </div>

  <div class="badges">
    <div class="badge" aria-label="Locally operated badge"></div>
    <div class="badge badge--gold" aria-label="Established year badge"></div>
  </div>

  <div class="web-band">vendracoffee.example</div>
</section>

</body>
</html>
```